Business card to be used as a flyer

This business card should do the trick of a full scale flyer , so basicaly from the business card itself we only keep the size and remove the clasical name , position , company name (etc).
This business cards should be , like said above, used as promo tool, being gived to different girls . So base one : the design is girls oriented.
Colors : black background . We will use gold (color) folio for the text.
Attached you have our logo, but this should not be a proiminent part of the design . You can use only the cat head instead.
Target Market(s)
Girls / Women
Contact Information for Business Card
> black background , gold / folio text and elements
> cat head from the logo in a creative way do be displayed
> proieminent text "your path to success starts here"
> contact details phone and website .
www.velmastrand.ro (website) and 0742163958 (phone)

```html
<!DOCTYPE html>
<html lang="en">
<head>
<meta charset="UTF-8">
<title>Velmastrand Studio – Promo Card</title>
<link href="https://fonts.googleapis.com/css2?family=Great+Vibes&family=Open+Sans:wght@700&family=Noto+Serif:wght@400&display=swap" rel="stylesheet">
<style>
  :root {
    --page-bg: #2a2d31;
    --card-black: #060606;
    --card-black-soft: #1a1a1a;
    --card-white: #ffffff;
    --gold: #d8a92e;
    --gold-light: #f3d36a;
    --gold-deep: #a97a12;
    --ink: #111111;
  }
  html, body {
    margin: 0;
    padding: 0;
    width: 1200px;
    height: 900px;
    overflow: hidden;
    background: var(--page-bg);
  }
  .canvas {
    position: relative;
    width: 1200px;
    height: 900px;
  }
  .card {
    position: absolute;
    top: 296px;
    width: 540px;
    height: 309px;
    overflow: hidden;
    box-shadow: 0 10px 30px rgba(0,0,0,0.45);
  }

  /* Front side */
  .card-front {
    left: 40px;
    background: var(--card-white);
  }
  .front-band {
    position: absolute;
    left: 0;
    right: 0;
    top: 150px;
    height: 86px;
    background: var(--card-black);
  }
  .front-gold-rule {
    position: absolute;
    left: 58px;
    top: 22px;
    width: 5px;
    height: 268px;
    background: linear-gradient(180deg, var(--gold-light), var(--gold), var(--gold-deep));
  }
  .brand-name {
    position: absolute;
    left: 105px;
    top: 62px;
    margin: 0;
    font-family: "Open Sans", sans-serif;
    font-weight: 700;
    font-size: 27px;
    letter-spacing: 1px;
    color: var(--ink);
    line-height: 1;
  }
  .brand-name .brand-sub {
    display: block;
    font-size: 13px;
    letter-spacing: 0.5px;
    text-align: right;
    margin-top: 3px;
  }
  .contact-list {
    position: absolute;
    left: 80px;
    top: 150px;
    height: 86px;
    display: flex;
    align-items: center;
    gap: 48px;
    margin: 0;
    padding: 0;
    list-style: none;
    font-family: "Noto Serif", serif;
    font-size: 21px;
    color: var(--gold);
  }
  .contact-item {
    display: flex;
    align-items: center;
    gap: 9px;
  }
  .contact-icon {
    width: 16px;
    height: 16px;
    fill: var(--gold);
  }

  /* Back side */
  .card-back {
    left: 620px;
    background:
      repeating-linear-gradient(90deg, rgba(255,255,255,0.015) 0 1px, transparent 1px 3px),
      radial-gradient(ellipse at 40% 35%, var(--card-black-soft), var(--card-black) 70%);
  }
  .tagline {
    position: absolute;
    left: 36px;
    top: 34px;
    margin: 0;
    font-family: "Great Vibes", cursive;
    font-weight: 400;
    font-size: 44px;
    line-height: 1.05;
    background: linear-gradient(180deg, var(--gold-light), var(--gold) 55%, var(--gold-deep));
    -webkit-background-clip: text;
    background-clip: text;
    color: transparent;
  }
  .tagline .tagline-line2 {
    display: block;
    padding-left: 0;
  }
  .feline-artwork {
    position: absolute;
    right: 24px;
    top: 90px;
    width: 230px;
    height: 219px;
    border-radius: 60% 40% 0 0;
    background: radial-gradient(ellipse at 60% 35%, rgba(216,169,46,0.55), rgba(169,122,18,0.25) 55%, rgba(6,6,6,0) 80%);
  }
</style>
</head>
<body>
<main class="canvas">

  <section class="card card-front" aria-label="Card front">
    <div class="front-band"></div>
    <div class="front-gold-rule"></div>
    <h1 class="brand-name">VELMASTRAND<span class="brand-sub">studio</span></h1>
    <ul class="contact-list">
      <li class="contact-item">
        <svg class="contact-icon" viewBox="0 0 24 24" aria-hidden="true">
          <path d="M6.6 10.8c1.4 2.8 3.8 5.1 6.6 6.6l2.2-2.2c.3-.3.7-.4 1-.2 1.1.4 2.3.6 3.6.6.6 0 1 .4 1 1V20c0 .6-.4 1-1 1C10.6 21 3 13.4 3 4c0-.6.4-1 1-1h3.5c.6 0 1 .4 1 1 0 1.3.2 2.5.6 3.6.1.3 0 .7-.2 1L6.6 10.8z"/>
        </svg>
        <span>0742163958</span>
      </li>
      <li class="contact-item">
        <svg class="contact-icon" viewBox="0 0 24 24" aria-hidden="true">
          <circle cx="12" cy="12" r="9" fill="none" stroke="#d8a92e" stroke-width="2"/>
          <path d="M3 12h18M12 3c3 3 3 15 0 18M12 3c-3 3-3 15 0 18" fill="none" stroke="#d8a92e" stroke-width="1.6"/>
        </svg>
        <span>www.velmastrand.ro</span>
      </li>
    </ul>
  </section>

  <section class="card card-back" aria-label="Card back">
    <h2 class="tagline">Your Path to<span class="tagline-line2">Success Starts Here</span></h2>
    <div class="feline-artwork" role="img" aria-label="Gold line illustration of a cat head and neck"></div>
  </section>

</main>
</body>
</html>
```